Door Knockers/Cards

Tallbrook Exteriors - EST 1986
Specialist in custom exterior remodeling solutions for your home and cottage.
Book your free estimate today.
Tallbrook Exteriors Inc.
(555) 482-7316
sales@tallbrookexteriors-example.com
Founded in 1986 in Elmira, Ontario, Tallbrook Exteriors has grown to become an industry-leading provider of siding, eavestrough, railings, columns, windows, doors, and garage doors.
Our expert team provides custom remodeling services across Ontario for a wide variety of residential and commercial projects. From traditional exterior home remodels to luxurious custom homes, agricultural facilities, places of worship, retail buildings, and industrial businesses, Tallbrook Exteriors does it all.
**Would like to have a QR code if possible for clients to be linked to our site right away.**

```html
<!DOCTYPE html>
<html lang="en">
<head>
<meta charset="utf-8">
<title>Tallbrook Exteriors Door Hangers</title>
<link href="https://fonts.googleapis.com/css2?family=Oswald:wght@400;500;600;700&family=Montserrat:ital,wght@0,400;0,500;0,600;1,600;1,700;1,800&display=swap" rel="stylesheet">
<style>
:root{
  --maroon:#652524;
  --beige:#cfb8a9;
  --ink:#4a4a4a;
  --white:#ffffff;
  --stage:#b5b7ba;
  --hole:#0b0b0b;
}
*{margin:0;padding:0;box-sizing:border-box}
html,body{width:1200px;height:2374px;overflow:hidden;background:var(--stage)}
.stage{position:relative;width:1200px;height:2374px}
.hanger{position:absolute;top:583px;width:520px;height:1208px;overflow:hidden;background:var(--white)}
.hanger--front{left:53px}
.hanger--back{left:627px}
.photo{position:absolute;left:0;top:0;width:520px;height:440px}
.photo--home{background:linear-gradient(180deg,#dfe6ee 0%,#b9c7d6 22%,#8d9a86 45%,#9a8f80 65%,#5f7a45 100%)}
.photo--hall{background:linear-gradient(180deg,#e6e9ee 0%,#c9cfd6 30%,#a9b0b8 60%,#8b8782 100%)}
.shapes{position:absolute;left:0;top:0}
.logo{position:absolute;left:0;width:520px;display:flex;align-items:center;justify-content:center;gap:12px;top:440px}
.logo-mark{width:30px;height:30px;background:var(--maroon)}
.logo-name{font-family:'Oswald',sans-serif;font-weight:600;font-size:32px;letter-spacing:1px;color:var(--ink);text-transform:uppercase}
.headline{position:absolute;left:0;top:505px;width:520px;text-align:center;font-family:'Oswald',sans-serif;text-transform:uppercase;line-height:1}
.headline-main{display:block;font-weight:700;font-size:104px;color:var(--maroon);letter-spacing:-1px}
.headline-sub{display:block;font-weight:700;font-size:70px;color:var(--maroon);letter-spacing:-0.5px;margin-top:-2px}
.headline-tag{display:block;font-weight:500;font-size:43px;color:var(--ink);margin-top:4px}
.tiles{position:absolute;top:767px;left:42px;width:436px;display:flex;justify-content:space-between}
.tile{width:134px;height:134px;border-radius:32px;border:3px solid var(--maroon)}
.tile--cabin{background:linear-gradient(160deg,#c9d3dc,#7a4a34 55%,#3f5a2f)}
.tile--hall{background:linear-gradient(160deg,#e3e7ec,#b7bec6 55%,#8e8a83)}
.tile--stone{background:linear-gradient(160deg,#dfe4ea,#d8c9a8 55%,#a8a090)}
.estimate{position:absolute;left:44px;top:932px;width:432px;height:64px;border-radius:14px;background:var(--beige);display:flex;align-items:center;justify-content:center;font-family:'Oswald',sans-serif;font-weight:500;font-size:32px;color:var(--white);text-transform:uppercase}
.contact{position:absolute;left:0;width:520px;text-align:center;font-family:'Montserrat',sans-serif;font-style:italic}
.contact-call{display:block;font-weight:700;font-size:26px;color:var(--white);text-transform:uppercase}
.contact-phone{display:block;font-weight:800;font-size:54px;color:var(--beige);line-height:1.1}
.contact-address{display:block;font-weight:600;font-size:14px;color:var(--white);margin-top:4px}
.contact-web{display:flex;align-items:center;justify-content:center;gap:6px;font-weight:600;font-size:16px;color:var(--white);margin-top:22px}
.hanger--front .contact{top:1032px}
.hanger--back .contact{top:1060px}
.services{position:absolute;left:48px;top:515px;width:430px}
.service{display:flex;justify-content:space-between;align-items:flex-start;height:99px}
.service-text{width:320px}
.service-title{font-family:'Oswald',sans-serif;font-weight:500;font-size:22px;color:var(--maroon);text-transform:uppercase;line-height:1.1}
.service-desc{font-family:'Montserrat',sans-serif;font-size:10.5px;color:var(--ink);line-height:1.3;margin-top:4px}
.thumb{width:80px;height:80px;border-radius:8px;border:2px solid var(--maroon)}
.thumb--cabin{background:linear-gradient(160deg,#c9d3dc,#7a4a34 55%,#3f5a2f)}
.thumb--hall{background:linear-gradient(160deg,#e3e7ec,#b7bec6 55%,#8e8a83)}
.thumb--stone{background:linear-gradient(160deg,#dfe4ea,#d8c9a8 55%,#a8a090)}
.thumb--entry{background:linear-gradient(180deg,#f2f2f2,#d9d9d9 60%,#5a5a5a)}
.residential{position:absolute;left:0;top:914px;width:520px;height:124px;background:var(--beige);text-align:center;padding-top:18px}
.residential-title{font-family:'Oswald',sans-serif;font-weight:600;font-size:36px;color:var(--maroon);text-transform:uppercase;line-height:1.1}
.residential-list{font-family:'Montserrat',sans-serif;font-size:13px;color:var(--ink);line-height:1.3;margin:6px auto 0;width:430px}
.call-band{position:absolute;left:0;top:1038px;width:520px;height:170px;background:var(--maroon)}
</style>
</head>
<body>
<main class="stage">

  <section class="hanger hanger--front" aria-label="Door hanger front">
    <div class="photo photo--home" role="img" aria-label="Photo of a large stone family home with trees and blue sky"></div>
    <svg class="shapes" width="520" height="1208" viewBox="0 0 520 1208" aria-hidden="true">
      <polygon points="0,416 260,296 520,416 520,440 260,318 0,440" fill="var(--maroon)"/>
      <polygon points="0,438 260,318 520,438 520,1208 0,1208" fill="var(--white)"/>
      <polygon points="0,900 260,812 520,900 520,1208 0,1208" fill="var(--maroon)"/>
      <line x1="104" y1="0" x2="230" y2="120" stroke="var(--hole)" stroke-width="6"/>
      <circle cx="260" cy="159" r="70" fill="var(--hole)"/>
    </svg>
    <div class="logo"><span class="logo-mark"></span><span class="logo-name">Tallbrook Exteriors Inc.</span></div>
    <h1 class="headline">
      <span class="headline-main">Exterior</span>
      <span class="headline-sub">Remodelling</span>
      <span class="headline-tag">Solutions Your Home</span>
    </h1>
    <div class="tiles">
      <div class="tile tile--cabin" role="img" aria-label="Photo of a wood-sided cottage"></div>
      <div class="tile tile--hall" role="img" aria-label="Photo of a grey-sided community hall"></div>
      <div class="tile tile--stone" role="img" aria-label="Photo of a stone commercial building"></div>
    </div>
    <div class="estimate">Book your free estimate today.</div>
    <div class="contact">
      <span class="contact-call">Call now today!</span>
      <span class="contact-phone">555-482-7316</span>
      <span class="contact-address">215 Harlow Road North Elmvale, ON N0A 3B7</span>
      <span class="contact-web">
        <svg width="18" height="18" viewBox="0 0 20 20" aria-hidden="true"><g fill="none" stroke="#fff" stroke-width="1.5"><circle cx="10" cy="10" r="8.5"/><ellipse cx="10" cy="10" rx="4" ry="8.5"/><line x1="1.5" y1="10" x2="18.5" y2="10"/></g></svg>
        www.tallbrookexteriors-example.com
      </span>
    </div>
  </section>

  <section class="hanger hanger--back" aria-label="Door hanger back">
    <div class="photo photo--hall" role="img" aria-label="Photo of a grey metal-sided hall with stone walkway"></div>
    <svg class="shapes" width="520" height="1208" viewBox="0 0 520 1208" aria-hidden="true">
      <polygon points="0,416 260,296 520,416 520,440 260,318 0,440" fill="var(--maroon)"/>
      <polygon points="0,438 260,318 520,438 520,1208 0,1208" fill="var(--white)"/>
      <line x1="414" y1="0" x2="290" y2="120" stroke="var(--hole)" stroke-width="6"/>
      <circle cx="260" cy="159" r="70" fill="var(--hole)"/>
    </svg>
    <div class="logo"><span class="logo-mark"></span><span class="logo-name">Tallbrook Exteriors Inc.</span></div>
    <div class="services">
      <div class="service">
        <div class="service-text">
          <h2 class="service-title">Siding</h2>
          <p class="service-desc">Our network of industry-leading manufacturers ensure that we can provide any type of siding imaginable to help you get the look you want for a price that works.</p>
        </div>
        <div class="thumb thumb--cabin" role="img" aria-label="Photo of a sided cottage"></div>
      </div>
      <div class="service">
        <div class="service-text">
          <h2 class="service-title">Soffit, Fascia, &amp; Eavestrough</h2>
          <p class="service-desc">Add practicality and beauty to the exterior of your business with professionally installed soffit, fascia, and eavestrough.</p>
        </div>
        <div class="thumb thumb--hall" role="img" aria-label="Photo of a hall roofline"></div>
      </div>
      <div class="service">
        <div class="service-text">
          <h2 class="service-title">Windows &amp; Doors</h2>
          <p class="service-desc">Transform the way people are welcomed into your business. Increase natural light and improve safety and energy-efficiency with new windows and doors.</p>
        </div>
        <div class="thumb thumb--stone" role="img" aria-label="Photo of building windows"></div>
      </div>
      <div class="service">
        <div class="service-text">
          <h2 class="service-title">Architectural Moulding and Trim</h2>
          <p class="service-desc">From ornate to contemporary, add style to your commercial building that will instantly help your business stand out.</p>
        </div>
        <div class="thumb thumb--entry" role="img" aria-label="Photo of a trimmed entrance door"></div>
      </div>
    </div>
    <div class="residential">
      <h2 class="residential-title">Residential Services</h2>
      <p class="residential-list">Siding | Eavestrough | Mouldings and Trims | Columns and Railings | Doors | Windows | Garage Doors</p>
    </div>
    <div class="call-band"></div>
    <div class="contact">
      <span class="contact-call">Call now today!</span>
      <span class="contact-phone">555-482-7316</span>
      <span class="contact-address">215 Harlow Road North Elmvale, ON N0A 3B7</span>
    </div>
  </section>

</main>
</body>
</html>
```